Shuffleboard Top graphic-Blending Several Country Flags

Hello, i am custom ordering a 12' shuffleboard for my home. My partner and I are both very proud of our heritage and i would like to incorporate our flags in the design for the top of the board, along with the USA flag, either all togerher or separating the three (USA, his flags and mine).

His nationality and country flags are Russia, Amenia and Moldova. Mine are Ireland, Italy, Germany and Hungary.

I'm envisioning either my 4 flags together on poles and his 3 flags together for two separate designs. OR, have the USA flag bleed into all of our flags in a linear design.

The design should be in a rectangle format and I can provide some estimated measurements.
Updates

Designs look the same

Target Market(s)

Friends and family

Requirements
Must have
• USA flags and our nationality flags: his-Russia, Armenia, Moldova. Mine-Italy, Ireland, Germany, Hungary
Nice to have
• Either his flags togerher as a group in one graphic and mine in a separate graphic. OR. All of our flags combined/blender together with the USA flag

```html
<!DOCTYPE html>
<html lang="en">
<head>
<meta charset="UTF-8">
<title>Heritage Flags Shuffleboard Top</title>
<style>
  :root {
    --armenia-red: #DC1F26;
    --armenia-blue: #233F9A;
    --armenia-orange: #F4A81F;
    --russia-white: #FFFFFF;
    --russia-blue: #22409B;
    --russia-red: #D72B25;
    --moldova-blue: #224FA3;
    --moldova-yellow: #FBD207;
    --moldova-red: #D01F30;
    --emblem-brown: #9C6B4E;
    --usa-red: #B32234;
    --usa-white: #FFFFFF;
    --usa-navy: #3C3B6E;
    --ireland-green: #1AA068;
    --ireland-orange: #F68B43;
    --hungary-red: #D22439;
    --hungary-green: #477655;
    --germany-black: #070809;
    --germany-red: #DE1F26;
    --germany-gold: #FCD20A;
    --italy-green: #0D984B;
    --italy-red: #D12A35;
    --white: #FFFFFF;
  }
  html, body {
    margin: 0;
    padding: 0;
    width: 1200px;
    height: 200px;
    overflow: hidden;
    background: var(--white);
  }
  .board-top { display: block; width: 1200px; height: 200px; }
  .star { fill: var(--usa-white); }
  .stripe-red { fill: var(--usa-red); }
  .stripe-white { fill: var(--usa-white); }
  .canton { fill: var(--usa-navy); }
</style>
</head>
<body>
<svg class="board-top" width="1200" height="200" viewBox="0 0 1200 200" xmlns="http://www.w3.org/2000/svg">
  <defs>
    <polygon id="star" class="star" points="0,-5 1.18,-1.62 4.76,-1.55 1.9,0.62 2.94,4.05 0,2 -2.94,4.05 -1.9,0.62 -4.76,-1.55 -1.18,-1.62"/>
  </defs>

  <!-- Russia and Armenia blended bands -->
  <g class="flag-russia-armenia">
    <rect x="0" y="0" width="200" height="33.4" style="fill:var(--armenia-red)"/>
    <rect x="0" y="33.3" width="200" height="33.4" style="fill:var(--armenia-blue)"/>
    <rect x="0" y="66.6" width="200" height="33.4" style="fill:var(--armenia-orange)"/>
    <rect x="0" y="99.9" width="200" height="33.4" style="fill:var(--russia-white)"/>
    <rect x="0" y="133.2" width="200" height="33.4" style="fill:var(--russia-blue)"/>
    <rect x="0" y="166.5" width="200" height="33.5" style="fill:var(--russia-red)"/>
  </g>

  <!-- Moldova -->
  <g class="flag-moldova">
    <rect x="200" y="0" width="66.8" height="200" style="fill:var(--moldova-blue)"/>
    <rect x="266.7" y="0" width="66.8" height="200" style="fill:var(--moldova-yellow)"/>
    <rect x="333.4" y="0" width="66.6" height="200" style="fill:var(--moldova-red)"/>
    <rect class="moldova-emblem" x="279" y="72" width="43" height="54" rx="8" style="fill:var(--emblem-brown)" role="img" aria-label="Moldovan coat of arms"/>
  </g>

  <!-- USA -->
  <g class="flag-usa">
    <rect class="stripe-red" x="400" y="0" width="400" height="200"/>
    <rect class="stripe-white" x="400" y="15.38" width="400" height="15.38"/>
    <rect class="stripe-white" x="400" y="46.15" width="400" height="15.38"/>
    <rect class="stripe-white" x="400" y="76.92" width="400" height="15.38"/>
    <rect class="stripe-white" x="400" y="107.69" width="400" height="15.38"/>
    <rect class="stripe-white" x="400" y="138.46" width="400" height="15.38"/>
    <rect class="stripe-white" x="400" y="169.23" width="400" height="15.38"/>
    <rect class="canton" x="400" y="0" width="152" height="107.7"/>
    <g class="stars">
      <use href="#star" x="412.6" y="9.8"/><use href="#star" x="438" y="9.8"/><use href="#star" x="463.4" y="9.8"/><use href="#star" x="488.8" y="9.8"/><use href="#star" x="514.2" y="9.8"/><use href="#star" x="539.6" y="9.8"/>
      <use href="#star" x="425.3" y="18.5"/><use href="#star" x="450.7" y="18.5"/><use href="#star" x="476.1" y="18.5"/><use href="#star" x="501.5" y="18.5"/><use href="#star" x="526.9" y="18.5"/>
      <use href="#star" x="412.6" y="27.1"/><use href="#star" x="438" y="27.1"/><use href="#star" x="463.4" y="27.1"/><use href="#star" x="488.8" y="27.1"/><use href="#star" x="514.2" y="27.1"/><use href="#star" x="539.6" y="27.1"/>
      <use href="#star" x="425.3" y="35.8"/><use href="#star" x="450.7" y="35.8"/><use href="#star" x="476.1" y="35.8"/><use href="#star" x="501.5" y="35.8"/><use href="#star" x="526.9" y="35.8"/>
      <use href="#star" x="412.6" y="44.4"/><use href="#star" x="438" y="44.4"/><use href="#star" x="463.4" y="44.4"/><use href="#star" x="488.8" y="44.4"/><use href="#star" x="514.2" y="44.4"/><use href="#star" x="539.6" y="44.4"/>
      <use href="#star" x="425.3" y="53.1"/><use href="#star" x="450.7" y="53.1"/><use href="#star" x="476.1" y="53.1"/><use href="#star" x="501.5" y="53.1"/><use href="#star" x="526.9" y="53.1"/>
      <use href="#star" x="412.6" y="61.8"/><use href="#star" x="438" y="61.8"/><use href="#star" x="463.4" y="61.8"/><use href="#star" x="488.8" y="61.8"/><use href="#star" x="514.2" y="61.8"/><use href="#star" x="539.6" y="61.8"/>
      <use href="#star" x="425.3" y="70.4"/><use href="#star" x="450.7" y="70.4"/><use href="#star" x="476.1" y="70.4"/><use href="#star" x="501.5" y="70.4"/><use href="#star" x="526.9" y="70.4"/>
      <use href="#star" x="412.6" y="79.1"/><use href="#star" x="438" y="79.1"/><use href="#star" x="463.4" y="79.1"/><use href="#star" x="488.8" y="79.1"/><use href="#star" x="514.2" y="79.1"/><use href="#star" x="539.6" y="79.1"/>
      <use href="#star" x="425.3" y="87.7"/><use href="#star" x="450.7" y="87.7"/><use href="#star" x="476.1" y="87.7"/><use href="#star" x="501.5" y="87.7"/><use href="#star" x="526.9" y="87.7"/>
      <use href="#star" x="412.6" y="96.4"/><use href="#star" x="438" y="96.4"/><use href="#star" x="463.4" y="96.4"/><use href="#star" x="488.8" y="96.4"/><use href="#star" x="514.2" y="96.4"/><use href="#star" x="539.6" y="96.4"/>
    </g>
  </g>

  <!-- Ireland -->
  <g class="flag-ireland">
    <rect x="800" y="0" width="66.8" height="100" style="fill:var(--ireland-green)"/>
    <rect x="866.7" y="0" width="66.8" height="100" style="fill:var(--white)"/>
    <rect x="933.4" y="0" width="66.6" height="100" style="fill:var(--ireland-orange)"/>
  </g>

  <!-- Hungary -->
  <g class="flag-hungary">
    <rect x="1000" y="0" width="200" height="33.4" style="fill:var(--hungary-red)"/>
    <rect x="1000" y="33.3" width="200" height="33.4" style="fill:var(--white)"/>
    <rect x="1000" y="66.6" width="200" height="33.4" style="fill:var(--hungary-green)"/>
  </g>

  <!-- Germany -->
  <g class="flag-germany">
    <rect x="800" y="100" width="200" height="33.4" style="fill:var(--germany-black)"/>
    <rect x="800" y="133.3" width="200" height="33.4" style="fill:var(--germany-red)"/>
    <rect x="800" y="166.6" width="200" height="33.4" style="fill:var(--germany-gold)"/>
  </g>

  <!-- Italy -->
  <g class="flag-italy">
    <rect x="1000" y="100" width="66.8" height="100" style="fill:var(--italy-green)"/>
    <rect x="1066.7" y="100" width="66.8" height="100" style="fill:var(--white)"/>
    <rect x="1133.4" y="100" width="66.6" height="100" style="fill:var(--italy-red)"/>
  </g>
</svg>
</body>
</html>
```